KVR Biz Cards

We are a property management company that manages luxury level residential estates. As such, we need a business card design that gives a high end feel. The idea at the moment is to list the services offered on the back of the card, and our company information on the front of the card.

Services for the back of the card are as follows:
Professional Property Management service, Home Hosting & Concierge Service, Holliday Home / Income Property Management

```html
<!DOCTYPE html>
<html lang="en">
<head>
<meta charset="utf-8">
<title>KVR Business Cards</title>
<link rel="stylesheet" href="https://fonts.googleapis.com/css2?family=Roboto:wght@400;500&display=swap">
<style>
  :root {
    --backdrop: #e3e3e3;
    --card: #ffffff;
    --bronze: #8b5e34;
    --ink: #2a2a2a;
  }
  * { margin: 0; padding: 0; box-sizing: border-box; }
  html, body { width: 1200px; height: 1200px; overflow: hidden; }
  body {
    background: var(--backdrop);
    font-family: "Roboto", Arial, sans-serif;
    color: var(--ink);
    position: relative;
  }
  .card {
    position: absolute;
    left: 189px;
    width: 830px;
    height: 474px;
    background: var(--card);
    border-radius: 28px;
    overflow: hidden;
    box-shadow: 0 6px 14px rgba(0,0,0,0.18);
  }
  .card--front { top: 100px; }
  .card--back { top: 634px; }
  .abs { position: absolute; line-height: 1; white-space: nowrap; }

  /* company name set as plain text, one colour, one weight */
  .brand {
    position: absolute;
    transform: translateX(-50%);
    text-align: center;
    color: var(--bronze);
    font-weight: 500;
    line-height: 1;
    white-space: nowrap;
  }
  .brand__initials { display: block; font-size: 60px; letter-spacing: 3px; }
  .brand__name { display: block; margin-top: 18px; font-size: 20px; letter-spacing: 1px; }

  /* front details */
  .divider { position: absolute; left: 411px; top: 110px; width: 2px; height: 256px; background: var(--bronze); }
  .person__name { left: 427px; top: 106px; font-size: 36px; font-weight: 500; color: var(--bronze); }
  .person__role { left: 427px; top: 146px; font-size: 18.5px; }
  .address { left: 427px; top: 196px; font-size: 18.5px; line-height: 32px; }
  .contact { left: 427px; display: flex; align-items: center; gap: 4px; font-size: 18.5px; }
  .contact svg { width: 18px; height: 18px; fill: var(--bronze); }
  .contact--phone { top: 280px; }
  .contact--mail { top: 311px; }
  .contact--web { top: 342px; }
  .bands { position: absolute; left: 0; top: 0; }
  .bands polygon { fill: var(--bronze); }

  /* back */
  .services__headline { left: 0; right: 0; top: 280px; text-align: center; font-size: 36px; font-weight: 500; color: var(--bronze); }
  .services__list { left: 0; right: 0; top: 358px; text-align: center; font-size: 18.5px; line-height: 32px; }
</style>
</head>
<body>

<section class="card card--front">
  <div class="brand" style="left:253px; top:190px;">
    <span class="brand__initials">KVR</span>
    <span class="brand__name">KESTREL VALE RESIDENCES</span>
  </div>

  <div class="divider"></div>
  <div class="abs person__name">DANIEL CRANE</div>
  <div class="abs person__role">Managing Director</div>
  <div class="abs address">1840 Harbor Crest Lane<br>Seacliff CA 90210</div>

  <div class="abs contact contact--phone">
    <svg viewBox="0 0 24 24"><path d="M6.6 10.8a15.1 15.1 0 0 0 6.6 6.6l2.2-2.2c.3-.3.7-.4 1-.2 1.1.4 2.3.6 3.6.6.6 0 1 .4 1 1V20c0 .6-.4 1-1 1A17 17 0 0 1 3 4c0-.6.4-1 1-1h3.5c.6 0 1 .4 1 1 0 1.3.2 2.5.6 3.6.1.3 0 .7-.2 1z"/></svg>
    <span>555 014 2290</span>
  </div>
  <div class="abs contact contact--mail">
    <svg viewBox="0 0 24 24"><path d="M2 5h20v2l-10 6L2 7z"/><path d="M2 9l10 6 10-6v10H2z"/></svg>
    <span>hello@kestrelvale.com</span>
  </div>
  <div class="abs contact contact--web">
    <svg viewBox="0 0 24 24"><circle cx="12" cy="12" r="10"/><path d="M12 2v20M2 12h20" stroke="#fff" stroke-width="1.5" fill="none"/></svg>
    <span>www.kestrelvale.com</span>
  </div>

  <svg class="bands" width="830" height="474" viewBox="0 0 830 474" aria-hidden="true">
    <polygon points="0,436 438,436 427,447 0,447"/>
    <polygon points="0,455 420,455 402,474 0,474"/>
    <polygon points="461,426 830,426 830,474 416,474"/>
  </svg>
</section>

<section class="card card--back">
  <div class="brand" style="left:415px; top:112px;">
    <span class="brand__initials">KVR</span>
    <span class="brand__name">KESTREL VALE RESIDENCES</span>
  </div>

  <div class="abs services__headline">Professional Property Management servic</div>
  <div class="abs services__list">Home Hosting &amp; Concierge Service,<br>Holliday Home / Income Property Management</div>
</section>

</body>
</html>
```